New sauce/condiment range label design

We need label design for bottles. Its a new range encompassing meat sauce, aioli type dressing, dessert sauce, vinaigrette etc.
The products will be sold in retail gourmet food outlets. They will appeal to a wide range of customers and be purchased for own use as well as gifts.

Reason: I'm away from email for this period so no need to hurry over this one! Thanks

Target Market(s)

pretty much everyone over 20yrs of age who appreciate great tasting foods

Industry/Entity Type

Retail

Requirements
Must have
• Must have company name, fern logo (which can be seperated from name and also different colours.
The label dimensions are 50mm high x 190mm wide.

```html
<!DOCTYPE html>
<html lang="en">
<head>
<meta charset="utf-8">
<title>Gourmet Collection – Seafood Sauce Labels</title>
<link rel="stylesheet" href="https://fonts.googleapis.com/css2?family=Cinzel:wght@400&family=Questrial&family=Archivo+Narrow:ital,wght@0,400;1,400&display=swap">
<style>
  :root {
    --page: #ffffff;
    --label-black: #0c0b0a;
    --label-ink: #f2efe8;
    --gold-rule: #b99a55;
    --fern-green: #3f5a1e;
    --fern-lime: #8fb33a;
    --berry: #7a1c2c;
    --berry-dark: #3c0c15;
    --ocean: #24408e;
    --ocean-dark: #0f1c45;
    --olive: #8a7a2c;
    --olive-dark: #3f3710;
  }
  * { box-sizing: border-box; margin: 0; padding: 0; }
  html, body { width: 1200px; height: 759px; overflow: hidden; background: var(--page); }
  .canvas { position: relative; width: 1200px; height: 759px; background: var(--page); }

  .label {
    position: absolute; top: 240px; width: 368px; height: 338px;
    background: var(--label-black); color: var(--label-ink); overflow: hidden;
  }
  .label--berry { left: 43px; --accent: var(--berry); --accent-dark: var(--berry-dark); }
  .label--ocean { left: 428px; --accent: var(--ocean); --accent-dark: var(--ocean-dark); }
  .label--olive { left: 800px; --accent: var(--olive); --accent-dark: var(--olive-dark); }

  .tagline {
    position: absolute; left: 58px; top: 26px;
    font-family: "Archivo Narrow", sans-serif; font-size: 15px; letter-spacing: 0.2px;
  }
  .range-name {
    position: absolute; left: 58px; top: 44px;
    font-family: "Questrial", sans-serif; font-size: 27px; letter-spacing: 0.3px;
  }
  .maker-tab {
    position: absolute; right: 10px; top: 12px; width: 26px; height: 82px;
    background: linear-gradient(90deg, var(--accent-dark), var(--accent));
    display: flex; align-items: center; justify-content: center;
  }
  .maker-tab span {
    transform: rotate(-90deg); white-space: nowrap;
    font-family: "Archivo Narrow", sans-serif; font-size: 12px; color: var(--label-ink);
  }
  .rule { position: absolute; height: 1px; background: var(--gold-rule); }
  .rule--top { left: 58px; right: 10px; top: 86px; }
  .rule--bottom { left: 142px; right: 10px; top: 228px; }

  .fern-mark {
    position: absolute; left: 0; top: 96px; width: 150px; height: 136px;
    background: radial-gradient(ellipse at 45% 50%, rgba(143,179,58,0.45), rgba(63,90,30,0.25) 55%, rgba(12,11,10,0) 80%);
  }
  .product-name {
    position: absolute; left: 142px; top: 124px;
    font-family: "Cinzel", serif; font-size: 40px; line-height: 40px; letter-spacing: 0.5px;
  }
  .descriptor {
    position: absolute; left: 146px; top: 208px;
    font-family: "Archivo Narrow", sans-serif; font-size: 14px;
  }
  .footer-band {
    position: absolute; left: 0; right: 0; top: 244px; height: 38px;
    background: linear-gradient(90deg, var(--accent) 0%, var(--accent-dark) 55%, var(--accent) 100%);
    display: flex; align-items: center; justify-content: space-between; padding: 0 12px;
    font-family: "Archivo Narrow", sans-serif; font-size: 12px;
  }
</style>
</head>
<body>
<main class="canvas">

  <section class="label label--berry">
    <p class="tagline">bringing joy to your tastebuds!</p>
    <h2 class="range-name">Gourmet Collection</h2>
    <div class="maker-tab"><span>Riverstone</span></div>
    <div class="rule rule--top"></div>
    <div class="fern-mark" role="img" aria-label="Fern leaf emblem in green tones"></div>
    <h1 class="product-name">SEAFOOD<br>SAUCE</h1>
    <p class="descriptor">Loremp Ipsum  sit amet</p>
    <div class="rule rule--bottom"></div>
    <div class="footer-band"><span>Made in New Zealand</span><span>NET WT 12 oz (355ml)</span></div>
  </section>

  <section class="label label--ocean">
    <p class="tagline">bringing joy to your tastebuds!</p>
    <h2 class="range-name">Gourmet Collection</h2>
    <div class="maker-tab"><span>Riverstone</span></div>
    <div class="rule rule--top"></div>
    <div class="fern-mark" role="img" aria-label="Fern leaf emblem in green tones"></div>
    <h1 class="product-name">SEAFOOD<br>SAUCE</h1>
    <p class="descriptor">Loremp Ipsum  sit amet</p>
    <div class="rule rule--bottom"></div>
    <div class="footer-band"><span>Made in New Zealand</span><span>NET WT 12 oz (355ml)</span></div>
  </section>

  <section class="label label--olive">
    <p class="tagline">bringing joy to your tastebuds!</p>
    <h2 class="range-name">Gourmet Collection</h2>
    <div class="maker-tab"><span>Riverstone</span></div>
    <div class="rule rule--top"></div>
    <div class="fern-mark" role="img" aria-label="Fern leaf emblem in green tones"></div>
    <h1 class="product-name">SEAFOOD<br>SAUCE</h1>
    <p class="descriptor">Loremp Ipsum  sit amet</p>
    <div class="rule rule--bottom"></div>
    <div class="footer-band"><span>Made in New Zealand</span><span>NET WT 12 oz (355ml)</span></div>
  </section>

</main>
</body>
</html>
```